New Stationary and Logo Design for Start Up Company

We need a logo design and stationary set including letterhead, business card (double sided), compliments slip and envelope for a new company Bright Quill Media.
The files should be editable to update address and standard contact details, will need to forward to web designer and stationary printer.
The company will be an online marketer and distributer of various business education products in Australia.
The designs should convey simple clean image
Target Market(s)
Small business owners and professional service providers (ie Accountants, Lawyers, Real Estate Agents) in Australia
Industry/Entity Type
Education
Look and feel
Each slider illustrates characteristics of the customer's brand and the style your logo design should communicate.

```html
<!DOCTYPE html>
<html lang="en">
<head>
<meta charset="utf-8">
<title>Bright Quill Media — Stationery Set</title>
<link rel="stylesheet" href="https://fonts.googleapis.com/css2?family=Open+Sans:wght@400;700&display=swap">
<style>
  :root {
    --brand-blue: #263a7a;
    --band-blue: #66739f;
    --brand-red: #d0202e;
    --paper: #ffffff;
    --ink: #1a1a1a;
    --page-bg: #ffffff;
    --edge: #3a3a3a;
  }
  * { box-sizing: border-box; margin: 0; padding: 0; }
  html, body { width: 1200px; height: 900px; overflow: hidden; background: var(--page-bg); }
  body { position: relative; font-family: "Open Sans", Arial, sans-serif; }

  .sheet {
    position: absolute;
    background: var(--paper);
    border: 1px solid var(--edge);
    box-shadow: 4px 4px 5px rgba(0,0,0,0.35);
    overflow: hidden;
  }
  .side-band { position: absolute; left: 0; top: 0; bottom: 0; background: var(--band-blue); }

  .wordmark {
    position: absolute;
    color: var(--brand-blue);
    font-weight: 400;
    text-transform: uppercase;
    white-space: nowrap;
    line-height: 1;
  }
  .person-name {
    position: absolute;
    color: var(--brand-red);
    font-weight: 700;
    letter-spacing: 3px;
    white-space: nowrap;
    line-height: 1;
  }
  .contact {
    position: absolute;
    font-weight: 700;
    font-size: 8px;
    letter-spacing: 1.4px;
    line-height: 13px;
    color: var(--ink);
    white-space: nowrap;
  }
  .contact .gap { display: block; height: 6px; }

  /* Letterhead */
  .letterhead { left: 45px; top: 75px; width: 533px; height: 753px; }
  .letterhead .side-band { width: 53px; }
  .letterhead .wordmark { left: 63px; top: 59px; font-size: 16px; }
  .letterhead .person-name { right: 24px; top: 66px; font-size: 10px; }
  .letterhead .contact { left: 63px; top: 650px; }

  /* Business card front */
  .card-front { left: 652px; top: 52px; width: 225px; height: 128px; }
  .card-front .side-band { width: 13px; }
  .card-front .wordmark { left: 54px; top: 68px; font-size: 12px; }

  /* Business card back */
  .card-back { left: 893px; top: 50px; width: 226px; height: 130px; }
  .card-back .back-field { position: absolute; left: 0; top: 0; right: 0; height: 108px; background: var(--brand-blue); }
  .card-back .contact { color: #fff; font-size: 7px; line-height: 11px; letter-spacing: 1.2px; top: 50px; }
  .card-back .contact.lines { right: 112px; text-align: right; }
  .card-back .contact.address { left: 125px; }
  .card-back .person-name { left: 0; right: 0; text-align: center; top: 113px; font-size: 8px; }

  /* Compliments slip */
  .compliments { left: 607px; top: 228px; width: 549px; height: 266px; }
  .compliments .side-band { width: 33px; }
  .compliments .wordmark { left: 50px; top: 52px; font-size: 18px; }
  .compliments .person-name { right: 18px; top: 18px; font-size: 10px; }
  .compliments .contact { right: 18px; top: 33px; text-align: right; line-height: 12px; font-size: 7.5px; }
  .compliments .greeting {
    position: absolute; left: 48px; top: 228px;
    color: var(--brand-red); font-size: 20px; letter-spacing: 1.5px; line-height: 1;
  }

  /* Envelope */
  .envelope { left: 604px; top: 543px; width: 555px; height: 137px; }
  .envelope .wordmark { left: 9px; top: 80px; font-size: 20px; }
  .envelope .divider {
    position: absolute; top: 6px; bottom: 10px; width: 2px;
    background: linear-gradient(to bottom, rgba(208,32,46,0), var(--brand-red) 50%, rgba(208,32,46,0));
  }
  .envelope .divider.first { left: 261px; }
  .envelope .divider.second { left: 418px; }
  .envelope .person-name { left: 272px; top: 64px; font-size: 12px; }
  .envelope .contact { left: 428px; top: 29px; font-size: 8.5px; line-height: 14px; }

  /* Master logotype */
  .master-logo {
    position: absolute; left: 638px; top: 806px; width: 480px;
    text-align: center; font-size: 40px;
  }
</style>
</head>
<body>

  <section class="sheet letterhead" aria-label="Letterhead">
    <div class="side-band"></div>
    <div class="wordmark">Bright Quill Media</div>
    <div class="person-name">Daniel Hart</div>
    <div class="contact">
      mailhere@mail.com<br>
      www.website.com<br>
      0112345678
      <span class="gap"></span>
      78 Addressstreet<br>
      Harbour Point<br>
      Australia
    </div>
  </section>

  <section class="sheet card-front" aria-label="Business card front">
    <div class="side-band"></div>
    <div class="wordmark">Bright Quill Media</div>
  </section>

  <section class="sheet card-back" aria-label="Business card back">
    <div class="back-field"></div>
    <div class="contact lines">0112345678<br>www.website.com<br>mailhere@mail.com</div>
    <div class="contact address">78 Addressstreet<br>Harbour Point<br>Australia</div>
    <div class="person-name">Daniel Hart</div>
  </section>

  <section class="sheet compliments" aria-label="Compliments slip">
    <div class="side-band"></div>
    <div class="wordmark">Bright Quill Media</div>
    <div class="person-name">Daniel Hart</div>
    <div class="contact">
      mailhere@mail.com<br>
      www.website.com<br>
      0112345678
      <span class="gap"></span>
      78 Addressstreet<br>
      Harbour Point<br>
      Australia
    </div>
    <p class="greeting">with compliments</p>
  </section>

  <section class="sheet envelope" aria-label="Envelope">
    <div class="wordmark">Bright Quill Media</div>
    <div class="divider first"></div>
    <div class="person-name">Daniel Hart</div>
    <div class="divider second"></div>
    <div class="contact">
      mailhere@mail.com<br>
      www.website.com<br>
      0112345678
      <span class="gap"></span>
      78 Addressstreet<br>
      Harbour Point<br>
      Australia
    </div>
  </section>

  <div class="wordmark master-logo">Bright Quill Media</div>

</body>
</html>
```